Harbor Grace Chapel Stationary and PPT template

Harbor Grace Chapel, an english-speaking church in urban Tokyo, Japan seeks a letterhead, envelope, and powerpoint background to communicate it's brand across all written and digital communications. The successful design should be conservative and classic in keeping with the church's long history as a beacon of light in Tokyo. A branding style guide should be consulted but designs should not emulate the mock design in the guide.

Designs should be classic and in keeping with the logo usage per the style guide. Colours should be faithful to the turquoise of the HGC brand.

The church website can be consulted for more information regarding phone numbers, address, etc.

Paper size- A4
Envelope size- DL
PPT Template- Mostly white background, colours at bottom + logo.

Target Market(s)

Outside vendors, members, prospective members.

Industry/Entity Type

Church

Requirements
Must have
• Church Logo, Address, phone, office email, white background.
Should not have
• contemporary look and feel. Must be classic design

```html
<!DOCTYPE html>
<html lang="en">
<head>
<meta charset="utf-8">
<title>Harbor Grace Chapel Stationery Set</title>
<link href="https://fonts.googleapis.com/css2?family=Ubuntu:wght@400;500;700&display=swap" rel="stylesheet">
<style>
  :root {
    --teal: #5bc6c7;
    --teal-deep: #2e6e70;
    --teal-pale: #c6ecec;
    --teal-dark-end: #1f6566;
    --paper: #ffffff;
    --backdrop: #2b2b2b;
    --white: #ffffff;
  }
  * { margin: 0; padding: 0; box-sizing: border-box; }
  html, body { width: 1200px; height: 1200px; overflow: hidden; }
  body {
    background: var(--backdrop);
    font-family: "Ubuntu", sans-serif;
    position: relative;
  }
  .back-sheet {
    position: absolute; left: 95px; top: 165px; width: 689px; height: 891px;
    background: var(--teal);
  }
  .sheet {
    position: absolute;
    background: var(--paper);
    overflow: hidden;
  }
  .sheet .wave {
    position: absolute; left: 0; top: 0; width: 100%; height: 100%;
  }
  .letterhead { left: 58px; top: 195px; width: 689px; height: 891px; }
  .envelope { left: 362px; top: 98px; width: 749px; height: 325px; }
  .slide { left: 618px; top: 481px; width: 493px; height: 370px; }

  .brand { position: absolute; color: var(--teal); text-align: center; }
  .brand-mark {
    width: 26px; height: 26px; background: var(--teal); margin: 0 auto 10px;
  }
  .brand-name {
    font-size: 10px; letter-spacing: 1.6px; font-weight: 400;
    padding-bottom: 5px; border-bottom: 1px solid var(--teal);
    white-space: nowrap;
  }
  .brand-tagline { font-size: 9px; letter-spacing: 1px; margin-top: 6px; }

  .letterhead .brand { left: 24px; top: 74px; }
  .envelope .brand { left: 31px; top: 74px; }
  .slide .brand { left: 292px; top: 184px; }

  .contact {
    position: absolute; display: flex; align-items: center; color: var(--white);
    white-space: nowrap;
  }
  .contact-lines { line-height: 1.25; }
  .contact-lines .key { display: inline-block; width: 20px; font-weight: 500; }
  .contact-divider {
    width: 1px; align-self: stretch; background: var(--white); margin: 8px 12px 0;
  }
  .contact-address { padding-top: 16px; line-height: 1.25; }
  .letterhead .contact { left: 24px; top: 820px; font-size: 13px; }
  .slide .contact { left: 26px; top: 312px; font-size: 9.5px; }
  .slide .contact .key { width: 14px; }
  .slide .contact-divider { margin: 6px 9px 0; }
  .slide .contact-address { padding-top: 11px; }

  .envelope-address {
    position: absolute; left: 75px; top: 278px;
    color: var(--white); font-size: 17px; font-weight: 500;
  }

  .slide-welcome {
    position: absolute; left: 40px; top: 34px;
    color: var(--teal); font-size: 44px; font-weight: 700;
  }
  .slide-title {
    position: absolute; left: 45px; top: 105px;
    color: var(--teal); font-size: 35px; font-weight: 500; line-height: 42px;
  }
  .slide-title span { display: block; }
  .slide-title span:nth-child(2) { padding-left: 32px; }
  .slide-title span:nth-child(3) { padding-left: 55px; }
</style>
</head>
<body>

<div class="back-sheet" aria-hidden="true"></div>

<section class="sheet letterhead" aria-label="Letterhead">
  <svg class="wave" viewBox="0 0 860 1115" preserveAspectRatio="none" aria-hidden="true">
    <path d="M0,985 C120,940 250,920 330,935 C480,960 600,1030 740,1028 C800,1027 840,990 860,955 L860,1115 L0,1115Z" fill="var(--teal)"/>
    <path d="M0,975 C120,930 250,910 330,925 C480,950 600,1020 740,1018 C800,1017 840,980 860,945" fill="none" stroke="var(--teal-deep)" stroke-width="6"/>
    <path d="M0,983 C120,938 250,918 330,933 C480,958 600,1028 740,1026" fill="none" stroke="var(--teal-pale)" stroke-width="3"/>
  </svg>
  <div class="brand">
    <div class="brand-mark"></div>
    <div class="brand-name">HARBOR GRACE CHAPEL</div>
    <div class="brand-tagline">Grace for every soul</div>
  </div>
  <div class="contact">
    <div class="contact-lines">
      <div><span class="key">T</span>: 123-456-7890</div>
      <div><span class="key">W</span>: www.harborgracechapel.com</div>
      <div><span class="key">E</span>: office@harborgracechapel.com</div>
    </div>
    <div class="contact-divider"></div>
    <div class="contact-address">
      <div>Dummy city</div>
      <div>Dummy country, land</div>
    </div>
  </div>
</section>

<section class="sheet envelope" aria-label="DL envelope">
  <svg class="wave" viewBox="0 0 936 406" preserveAspectRatio="none" aria-hidden="true">
    <path d="M0,345 C100,310 200,285 280,288 C420,292 560,385 720,388 C820,390 890,345 936,308 L936,406 L0,406Z" fill="var(--teal)"/>
    <path d="M0,338 C100,303 200,278 280,281 C420,285 560,378 720,381 C820,383 890,338 936,301" fill="none" stroke="var(--teal-deep)" stroke-width="5"/>
    <path d="M0,344 C100,309 200,284 280,287 C420,291 560,384 720,387" fill="none" stroke="var(--teal-pale)" stroke-width="3"/>
  </svg>
  <div class="brand">
    <div class="brand-mark"></div>
    <div class="brand-name">HARBOR GRACE CHAPEL</div>
    <div class="brand-tagline">Grace for every soul</div>
  </div>
  <div class="envelope-address">Dummy city, Dummy country, land</div>
</section>

<section class="sheet slide" aria-label="Presentation slide">
  <svg class="wave" viewBox="0 0 616 462" preserveAspectRatio="none" aria-hidden="true">
    <defs>
      <linearGradient id="slideBand" x1="0" y1="0" x2="1" y2="0">
        <stop offset="0" stop-color="var(--teal)"/>
        <stop offset="1" stop-color="var(--teal-dark-end)"/>
      </linearGradient>
    </defs>
    <path d="M0,365 C70,335 130,318 200,320 C320,325 400,385 500,382 C560,380 600,350 616,325 L616,462 L0,462Z" fill="url(#slideBand)"/>
    <path d="M0,358 C70,328 130,311 200,313 C320,318 400,378 500,375 C560,373 600,343 616,318" fill="none" stroke="var(--teal-deep)" stroke-width="4"/>
    <path d="M0,363 C70,333 130,316 200,318 C320,323 400,383 500,380" fill="none" stroke="var(--white)" stroke-width="2.5"/>
  </svg>
  <div class="slide-welcome">WELCOME</div>
  <div class="slide-title">
    <span>HARBOR</span>
    <span>GRACE</span>
    <span>CHAPEL</span>
  </div>
  <div class="brand">
    <div class="brand-mark"></div>
    <div class="brand-name">HARBOR GRACE CHAPEL</div>
    <div class="brand-tagline">Grace for every soul</div>
  </div>
  <div class="contact">
    <div class="contact-lines">
      <div><span class="key">T</span>: 123-456-7890</div>
      <div><span class="key">W</span>: www.harborgracechapel.com</div>
      <div><span class="key">E</span>: office@harborgracechapel.com</div>
    </div>
    <div class="contact-divider"></div>
    <div class="contact-address">
      <div>Dummy city</div>
      <div>Dummy country, land</div>
    </div>
  </div>
</section>

</body>
</html>
```